KV MERCANTILE HOLDINGS LETTERHEAD

I need letterhead for "KV Mercantile holdings LLC" ...

logo attached to project...

Company Info:
418 North Larkmoor Avenue, Suite 7B
Chicago, Illinois 60417
ofc 312-555-0148
facsimile 312-555-0193
www.kvmercantileholdings.example
info@kvmercantileholdings.example

I have multiple projects listed.. see below:

Business cards for amber ledge partners llc
letterhead
envelopes

Business cards for KV Mercantile LLC
letterhead
envelopes

```html
<!DOCTYPE html>
<html lang="en">
<head>
<meta charset="utf-8">
<title>KV Mercantile Holdings Letterhead</title>
<link href="https://fonts.googleapis.com/css2?family=Cinzel:wght@500&family=Roboto:wght@400&display=swap" rel="stylesheet">
<style>
  :root {
    --backdrop: #58585a;
    --paper: #ffffff;
    --brand-navy: #15426f;
    --swoosh-grey: #c9c9cb;
    --footer-text: #ffffff;
  }
  * { margin: 0; padding: 0; box-sizing: border-box; }
  html, body {
    width: 1200px;
    height: 1000px;
    overflow: hidden;
    background: var(--backdrop);
  }
  .letterhead {
    position: absolute;
    left: 295px;
    top: 85px;
    width: 600px;
    height: 845px;
    background: var(--paper);
    overflow: hidden;
  }
  .brand {
    position: absolute;
    right: 38px;
    top: 92px;
    text-align: right;
    color: var(--brand-navy);
  }
  .brand-name {
    font-family: "Cinzel", serif;
    font-weight: 500;
    font-size: 15px;
    letter-spacing: 0.3px;
    line-height: 1.1;
  }
  .brand-web {
    font-family: "Roboto", sans-serif;
    font-size: 9.5px;
    letter-spacing: 2.2px;
    margin-top: 4px;
  }
  .footer-shape {
    position: absolute;
    left: 0;
    bottom: 0;
    width: 600px;
    height: 110px;
  }
  .footer-contact {
    position: absolute;
    left: 0;
    right: 0;
    bottom: 14px;
    text-align: center;
    font-family: "Roboto", sans-serif;
    font-size: 10.5px;
    line-height: 14px;
    color: var(--footer-text);
    padding-left: 55px;
  }
</style>
</head>
<body>
  <main class="letterhead">
    <header class="brand">
      <div class="brand-name">KV Mercantile Holdings LLC</div>
      <div class="brand-web">www.kvmercantileholdings.example</div>
    </header>

    <svg class="footer-shape" viewBox="0 0 600 110" aria-hidden="true">
      <defs>
        <linearGradient id="swoosh-fade" x1="0" x2="1" y1="0" y2="0">
          <stop offset="0" stop-color="var(--swoosh-grey)"/>
          <stop offset="0.7" stop-color="#e6e6e8"/>
          <stop offset="1" stop-color="#ffffff"/>
        </linearGradient>
      </defs>
      <path class="swoosh" d="M0 0 Q300 45 600 22 Q300 38 0 15 Z" fill="url(#swoosh-fade)"/>
      <path class="band" d="M0 9 Q300 50 600 22 L600 110 L0 110 Z" fill="var(--brand-navy)"/>
    </svg>

    <footer class="footer-contact">
      <div class="address">418 North Larkmoor Avenue, Suite 7B Chicago, Illinois 60417</div>
      <div class="lines">Office: 312-555-0148 | Facsimile: 312-555-0193 | Email: info@kvmercantileholdings.example</div>
    </footer>
  </main>
</body>
</html>
```